Zentro - revolutionary mobile payment

The app is a P2P money trasfert, without the using of credit card or bank circuits it can transfer electronic money from one person to another consumers simply and immediatelly.
You can use the color you want, but the message we need to transert to consumer is simplicity, safety and coolness.
In attach the logo of the company and the wireframe of thre page of the app.
The goal is to design the page of the app with a clear, simple and intuitive graphic.
Updates

I have upgrade the brief with important information and detail, many thanks

Target Market(s)

all the people

Industry/Entity Type

Credit Card

Requirements
Must have
• You have to design one icon for each button in the first page, (shop is: where to shop)
in the second one a new intuitive image (instead of the hand) that let the user to understand that with a simple swipe he can process the payment
Nice to have
• You can include or esxclude what you want or belive can improve user experience of the app
Should not have
• too much color, too much button or information

```html
<!DOCTYPE html>
<html lang="en">
<head>
<meta charset="utf-8">
<title>Zentro – mobile payment app</title>
<link href="https://fonts.googleapis.com/css2?family=Raleway:wght@300;400;500;600;700;800&display=swap" rel="stylesheet">
<style>
:root{
  --bg:#e6f0fc;
  --navy:#17306b;
  --navy-dark:#0f2356;
  --tile:#c9dcf3;
  --band:#c6daf2;
  --line:#9fb6d6;
  --text:#555a63;
  --ink:#1d2a44;
  --white:#ffffff;
}
*{box-sizing:border-box;margin:0;padding:0}
html,body{width:960px;height:1200px;overflow:hidden}
body{background:var(--bg);font-family:'Raleway',sans-serif;color:var(--ink);position:relative}

.brand{position:absolute;left:52px;top:36px;display:flex;align-items:center;gap:14px}
.brand-dot{width:78px;height:78px;border-radius:50%;background:var(--navy)}
.brand-name{font-size:66px;font-weight:800;color:var(--navy);letter-spacing:1px;line-height:1}
.intro{position:absolute;left:60px;top:146px;width:440px;font-size:15.5px;font-weight:300;line-height:21px;color:var(--text)}

.screen{position:absolute;width:174px;height:308px;overflow:hidden;
  background:radial-gradient(ellipse at 50% 40%,#f3f8fe 0%,#dbe7f6 60%,#bccfe8 100%);
  box-shadow:0 6px 20px rgba(15,35,86,.18)}
.screen.plain{background:#e3eefb}
.loading{left:560px;top:70px;width:250px;height:440px}
.loading .logo-mark{position:absolute;left:0;right:0;top:170px;justify-content:center}
.logo-mark{display:flex;align-items:center;gap:6px}
.logo-mark .dot{border-radius:50%;background:var(--navy)}
.logo-mark .name{font-weight:800;color:var(--navy);line-height:1}
.loading .dot{width:36px;height:36px}
.loading .name{font-size:32px}
.progress{position:absolute;left:45px;top:228px;width:160px;height:10px;border:1px solid var(--navy);background:var(--white)}
.progress span{display:block;width:45%;height:100%;background:var(--navy)}
.progress-label{position:absolute;left:45px;top:242px;font-size:8px;color:var(--navy)}

.s1{left:43px;top:716px}
.s2{left:274px;top:716px}
.s3{left:512px;top:716px}
.s4{left:745px;top:716px}

.s1 .logo-mark{position:absolute;top:80px;left:0;right:0;justify-content:center}
.s1 .dot{width:30px;height:30px}
.s1 .name{font-size:27px}
.field{position:absolute;left:5px;width:165px;height:23px;background:rgba(255,255,255,.75);border:1px solid var(--line);font-size:7.5px;padding:7px 0 0 15px;color:var(--ink)}
.btn{position:absolute;background:var(--navy);color:var(--white);font-size:7.5px;font-weight:500;display:flex;align-items:center;justify-content:center}
.btn.ghost{background:var(--white);color:var(--navy);border:1px solid var(--navy)}
.tiny{position:absolute;font-size:5.5px;color:var(--ink);display:flex;align-items:center;gap:4px}
.tiny u{text-decoration:underline}
.ring{width:8px;height:8px;border:1px solid var(--ink);border-radius:50%;font-size:6px;display:inline-flex;align-items:center;justify-content:center}
.signup{position:absolute;left:0;right:0;top:283px;font-size:7px;color:#4a5670;display:flex;justify-content:center;align-items:center;gap:5px}
.signup .ring{width:11px;height:11px}

.topbar{position:absolute;left:0;top:0;width:100%;height:19px;background:var(--navy);color:var(--white);display:flex;align-items:center;justify-content:space-between;padding:0 6px;font-size:6px}
.topbar .logo-mark{position:absolute;left:50%;transform:translateX(-50%)}
.topbar .dot{width:10px;height:10px;background:var(--white)}
.topbar .name{font-size:8px;color:var(--white)}
.menu-icon{width:8px;height:6px;border-top:1px solid #fff;border-bottom:1px solid #fff;position:relative}
.menu-icon::after{content:"";position:absolute;left:0;right:0;top:1.5px;border-top:1px solid #fff}
.band{position:absolute;left:0;top:19px;width:100%;height:46px;background:var(--band);display:flex;align-items:center;padding-left:8px;gap:16px}
.avatar{width:34px;height:34px;border-radius:50%;background:radial-gradient(circle at 50% 40%,#c89a80,#7a5a48);border:2px solid #fff}
.band h2{font-size:11.5px;font-weight:500}
.band h2 small{display:block;font-size:10.5px;font-weight:400}

.tile{position:absolute;width:76px;height:96px;background:var(--tile);display:flex;flex-direction:column;align-items:center;justify-content:center;gap:8px;font-size:13px;color:var(--ink)}
.tile svg{width:30px;height:30px}

.pay-head{position:absolute;left:0;top:19px;width:100%;height:26px;background:var(--band);display:flex;align-items:center;justify-content:center;font-size:11.5px}
.pay-head svg{position:absolute;left:9px;top:4px;width:16px;height:16px}
.input{position:absolute;top:50px;height:18px;border:1px solid var(--line);background:rgba(255,255,255,.6);font-size:6px;padding:5px 0 0 8px;color:#4a5670}
.amount{position:absolute;left:0;right:0;top:74px;text-align:center;font-size:15px;font-weight:700;color:var(--navy-dark);word-spacing:8px}
.note{position:absolute;left:5px;right:5px;top:101px;font-size:4.5px;color:#4a5670;border-bottom:1px solid var(--line);padding-bottom:2px}
.keypad{position:absolute;left:4px;top:112px;width:165px;display:grid;grid-template-columns:repeat(3,1fr);grid-auto-rows:38px;gap:2px}
.key{background:var(--tile);display:flex;flex-direction:column;align-items:center;justify-content:center;font-size:14px;color:var(--navy-dark);line-height:1.1}
.key small{font-size:6px}
.key.zero{grid-column:span 2}

.select{position:absolute;left:5px;top:78px;width:164px;height:17px;border:1px solid var(--line);background:rgba(255,255,255,.7);font-size:6px;padding:4px 0 0 6px;color:#4a5670}
.select::after{content:"";position:absolute;right:6px;top:6px;border:3px solid transparent;border-top:4px solid var(--ink)}
.tx{position:absolute;left:5px;width:164px;height:19px;background:var(--navy);color:var(--white);font-size:6px;display:flex;align-items:center;padding:0 6px;gap:6px}
.tx .person{width:7px;height:7px}
.tx .chev{margin-left:auto;font-size:8px}
</style>
</head>
<body>

<header class="brand">
  <span class="brand-dot"></span>
  <span class="brand-name">Zentro</span>
</header>
<p class="intro">The app is a P2P money trasfert, without the using of credit card or bank circuits it can transfer electronic money from one person to another consumers simply and immediatelly.</p>

<section class="screen loading" aria-label="Loading screen">
  <div class="logo-mark"><span class="dot"></span><span class="name">Zentro</span></div>
  <div class="progress"><span></span></div>
  <div class="progress-label">Loading...</div>
</section>

<section class="screen s1" aria-label="Login screen">
  <div class="logo-mark"><span class="dot"></span><span class="name">Zentro</span></div>
  <div class="field" style="top:142px">Username:</div>
  <div class="field" style="top:164px">Password:</div>
  <div class="btn" style="left:5px;top:196px;width:165px;height:22px">Log in</div>
  <div class="tiny" style="left:40px;top:229px">Remember me <span class="ring">✓</span> <u>Forgot password?</u></div>
  <div class="signup">Don't have an account? <span class="ring">+</span></div>
</section>

<section class="screen plain s2" aria-label="Main menu screen">
  <div class="topbar"><span>‹</span><div class="logo-mark"><span class="dot"></span><span class="name">Zentro</span></div><span class="menu-icon"></span></div>
  <div class="band"><span class="avatar" role="img" aria-label="User profile photo"></span><h2>Main Menu</h2></div>
  <div class="tile" style="left:7px;top:86px">
    <svg viewBox="0 0 30 30"><rect x="6" y="4" width="16" height="20" rx="2" fill="var(--navy)" transform="rotate(-20 14 14)"/><circle cx="14" cy="13" r="4" fill="#fff"/><rect x="8" y="22" width="16" height="6" rx="2" fill="var(--navy)"/></svg>
    Pay</div>
  <div class="tile" style="left:90px;top:86px">
    <svg viewBox="0 0 30 30"><path d="M15 2 L27 7 V16 C27 22 21 27 15 29 C9 27 3 22 3 16 V7 Z" fill="var(--navy)"/><text x="15" y="20" text-anchor="middle" font-size="13" font-weight="700" fill="#fff" font-family="Raleway,sans-serif">?</text></svg>
    Ask</div>
  <div class="tile" style="left:7px;top:190px">
    <svg viewBox="0 0 30 30"><path d="M11 4 H19 L17 9 C24 12 27 18 25 24 C24 27 21 28 15 28 C9 28 6 27 5 24 C3 18 6 12 13 9 Z" fill="var(--navy)"/><text x="15" y="24" text-anchor="middle" font-size="11" font-weight="700" fill="#fff" font-family="Raleway,sans-serif">$</text></svg>
    Account</div>
  <div class="tile" style="left:90px;top:190px">
    <svg viewBox="0 0 30 30" fill="none" stroke="var(--navy)" stroke-width="2.5"><path d="M2 5 H7 L10 20 H24 L27 9 H8"/><path d="M12 13 H25"/><circle cx="12" cy="25" r="2" fill="var(--navy)"/><circle cx="22" cy="25" r="2" fill="var(--navy)"/></svg>
    Shop</div>
</section>

<section class="screen plain s3" aria-label="Pay screen">
  <div class="topbar"><span>‹ Back</span><div class="logo-mark"><span class="dot"></span><span class="name">Zentro</span></div><span class="menu-icon"></span></div>
  <div class="pay-head"><svg viewBox="0 0 30 30"><rect x="6" y="4" width="16" height="20" rx="2" fill="var(--navy)" transform="rotate(-20 14 14)"/><circle cx="14" cy="13" r="4" fill="#fff"/><rect x="8" y="22" width="16" height="6" rx="2" fill="var(--navy)"/></svg>Pay</div>
  <div class="input" style="left:5px;width:38px">+39</div>
  <div class="input" style="left:46px;width:123px">Phone No:</div>
  <div class="amount">$ 0.00</div>
  <div class="note">Inserisci note (opzionale)</div>
  <div class="keypad">
    <div class="key">1</div><div class="key">2<small>ABC</small></div><div class="key">3<small>DEF</small></div>
    <div class="key">4<small>GHI</small></div><div class="key">5<small>JKL</small></div><div class="key">6<small>MNO</small></div>
    <div class="key">7<small>PQRS</small></div><div class="key">8<small>TUV</small></div><div class="key">9<small>WXYZ</small></div>
    <div class="key zero">0</div>
    <div class="key"><svg width="16" height="10" viewBox="0 0 16 10"><path d="M5 0 H16 V10 H5 L0 5 Z" fill="var(--navy)"/><path d="M8 3 L12 7 M12 3 L8 7" stroke="#fff" stroke-width="1.4"/></svg></div>
  </div>
  <div class="btn" style="left:5px;top:277px;width:164px;height:19px">Send</div>
</section>

<section class="screen plain s4" aria-label="Balance screen">
  <div class="topbar"><span>‹ Back</span><div class="logo-mark"><span class="dot"></span><span class="name">Zentro</span></div><span class="menu-icon"></span></div>
  <div class="band" style="gap:10px"><span class="avatar" role="img" aria-label="User profile photo"></span><h2>Your Balance<small>$ 106.82</small></h2></div>
  <div class="select">Last 30 days</div>
  <div class="tx" style="top:103px"><svg class="person" viewBox="0 0 8 8" fill="#fff"><circle cx="4" cy="2.2" r="2"/><path d="M0 8 C0 5 8 5 8 8Z"/></svg>+00555010123 &nbsp;$ 45<span class="chev">›</span></div>
  <div class="tx" style="top:126px"><svg class="person" viewBox="0 0 8 8" fill="#fff"><circle cx="4" cy="2.2" r="2"/><path d="M0 8 C0 5 8 5 8 8Z"/></svg>+00555010123 &nbsp;$ -45<span class="chev">›</span></div>
  <div class="tx" style="top:149px"><svg class="person" viewBox="0 0 8 8" fill="#fff"><circle cx="4" cy="2.2" r="2"/><path d="M0 8 C0 5 8 5 8 8Z"/></svg>+00555010123 &nbsp;$ 75<span class="chev">›</span></div>
  <div class="tx" style="top:172px"><svg class="person" viewBox="0 0 8 8" fill="#fff"><circle cx="4" cy="2.2" r="2"/><path d="M0 8 C0 5 8 5 8 8Z"/></svg>+00555010123 &nbsp;$ -65<span class="chev">›</span></div>
  <div class="tx" style="top:195px"><svg class="person" viewBox="0 0 8 8" fill="#fff"><circle cx="4" cy="2.2" r="2"/><path d="M0 8 C0 5 8 5 8 8Z"/></svg>+00555010123 &nbsp;$ 75<span class="chev">›</span></div>
  <div class="tx" style="top:218px"><svg class="person" viewBox="0 0 8 8" fill="#fff"><circle cx="4" cy="2.2" r="2"/><path d="M0 8 C0 5 8 5 8 8Z"/></svg>+00555010123 &nbsp;$ -65<span class="chev">›</span></div>
  <div class="btn" style="left:5px;top:269px;width:79px;height:18px">Report</div>
  <div class="btn ghost" style="left:91px;top:269px;width:79px;height:18px">Pocket</div>
</section>

</body>
</html>
```